Product label design needed for an odor removal line of products.

I need a label designed for an odor removal product line. There are eight additional odor removal products that I will need labels designed for so the winner will have additional work from me. I would like each of those products to have a similar look and feel in each one. This contest is for one of the products. The Brightwell 417 (would love a better name if you are so inclined -many people know what it is by the 417). The no smell formula does not mask odors, it eliminates odors at their source . Also Reduces Allergens! Simply open silver packet and place in dispenser. Great for use in cars, near pet beds or litter boxes, near diaper pails -anywhere odors are a problem. Lasts 60-90 days. Safe to use. Other uses: Nursing homes, hotel rooms, locker rooms, teenage boy rooms, basements... Eco Friendly! No VOC's or phthalates! Do not consume. Keep out of reach of children and pets. Replace every 60-90 days. I put the picture of my logo , the product as it is packaged and a picture of the actual product and the dispenser it will go in. the package is 4x5 in silver packet with .25 seam on the side and .5 seam on the top and bottom. (Dispenser will have a label with reorder information on it. to be designed later) You do not have to put all information provided on the label. It is to be used as you see fit. I tend to like clean, bold designs but am open to all options. Prefer not to use word air freshener.

Target Market(s)

Men and women between 30-65

Industry/Entity Type

Cleaning Product

Font styles to use
Sans Serif

Colors
acd136
9bcb3c
ffffff

Requirements
Must have
• ability for concept/look to be used for a laundry product, smaller odor elimination pouch, odor removing canister and spray as well
Nice to have
• I like greens but am open to designers to decide
Should not have
• word air freshener

```html
<!DOCTYPE html>
<html lang="en">
<head>
<meta charset="utf-8">
<title>Brightwell 417 – Packet Label</title>
<link rel="stylesheet" href="https://fonts.googleapis.com/css2?family=Roboto:wght@400;700;900&family=Oswald:wght@500&family=Dancing+Script:wght@600&display=swap">
<style>
  :root {
    --page-bg: #f8f8f8;
    --seam: #b9b9b9;
    --panel: #c4c4c4;
    --panel-light: #e6e6e6;
    --lime: #acd136;
    --leaf: #9bcb3c;
    --deep-green: #138a3a;
    --sky: #2f8cf0;
    --ink: #333333;
    --white: #ffffff;
  }
  * { margin: 0; padding: 0; box-sizing: border-box; }
  html, body { width: 1200px; height: 1000px; overflow: hidden; background: var(--page-bg); }
  .canvas { position: relative; width: 1200px; height: 1000px; }

  .packet {
    position: absolute; top: 212px; width: 461px; height: 576px;
    background: var(--seam);
    box-shadow: 0 30px 24px -22px rgba(0,0,0,0.25);
  }
  .packet--front { left: 99px; }
  .packet--back { left: 640px; }

  .packet__panel {
    position: absolute; left: 43px; top: 58px; width: 375px; height: 462px;
    background: var(--panel); overflow: hidden;
  }

  .swirl-art {
    position: absolute; border-radius: 50%;
    background: radial-gradient(circle at 50% 50%, var(--panel-light) 0%, rgba(155,203,60,0.35) 45%, rgba(47,140,240,0.3) 62%, rgba(196,196,196,0) 72%);
  }
  .packet--front .swirl-art { left: 12px; top: 46px; width: 350px; height: 350px; }
  .packet--back .swirl-art { left: 12px; top: 70px; width: 370px; height: 370px;
    background: radial-gradient(circle at 45% 50%, var(--panel-light) 0%, rgba(47,140,240,0.35) 40%, rgba(155,203,60,0.35) 60%, rgba(196,196,196,0) 72%); }

  /* Front */
  .brand-lockup {
    position: absolute; left: 0; right: 0; top: 160px;
    display: flex; flex-direction: column; align-items: center; gap: 8px;
  }
  .product-number {
    font-family: "Roboto", sans-serif; font-weight: 900; font-size: 72px;
    color: var(--deep-green); line-height: 1; letter-spacing: -2px;
  }
  .brand-name {
    display: flex; align-items: center; gap: 8px;
    font-family: "Roboto", sans-serif; font-weight: 700; font-size: 30px;
    color: var(--deep-green); letter-spacing: 1px;
  }
  .brand-name__dot { width: 18px; height: 18px; border-radius: 50%; background: var(--lime); }

  .tagline-ribbon {
    position: absolute; left: 90px; top: 348px; width: 196px; height: 30px;
    background: var(--deep-green); border: 1px solid var(--leaf);
    color: var(--white); font-family: "Roboto", sans-serif; font-size: 13px;
    display: flex; align-items: center; justify-content: center; letter-spacing: 0.2px;
  }
  .tagline-ribbon::before, .tagline-ribbon::after {
    content: ""; position: absolute; top: 6px; width: 24px; height: 26px; background: var(--leaf); z-index: -1;
  }
  .tagline-ribbon::before { left: -20px; }
  .tagline-ribbon::after { right: -20px; }

  /* Back */
  .eco-headline {
    position: absolute; left: 0; right: 0; top: 8px; text-align: center;
    font-family: "Dancing Script", cursive; font-weight: 600; font-size: 64px;
    color: var(--ink); transform: rotate(-3deg);
  }
  .brand-mark-small {
    position: absolute; left: 86px; top: 222px;
    display: flex; align-items: center; gap: 6px;
    font-family: "Roboto", sans-serif; font-weight: 700; font-size: 18px; color: var(--deep-green);
  }
  .brand-mark-small__dot { width: 12px; height: 12px; border-radius: 50%; background: var(--lime); }

  .usage-note {
    position: absolute; left: 52px; right: 52px; top: 394px; padding-bottom: 8px;
    border-bottom: 1px solid var(--ink);
    font-family: "Roboto", sans-serif; font-size: 22px; color: var(--ink); text-align: center;
  }
  .safety-warning {
    position: absolute; left: 0; right: 0; top: 434px; text-align: center;
    font-family: "Oswald", sans-serif; font-weight: 500; font-size: 14px; color: var(--ink);
  }
</style>
</head>
<body>
<main class="canvas">
  <section class="packet packet--front" aria-label="Packet front">
    <div class="packet__panel">
      <div class="swirl-art" role="img" aria-label="Halftone dot swirl in green and blue"></div>
      <div class="brand-lockup">
        <span class="product-number">417</span>
        <span class="brand-name"><span class="brand-name__dot"></span>Clearhaven</span>
      </div>
      <div class="tagline-ribbon">THE ODOR ELIMINATOR</div>
    </div>
  </section>

  <section class="packet packet--back" aria-label="Packet back">
    <div class="packet__panel">
      <div class="swirl-art" role="img" aria-label="Halftone dot swirl in blue and green"></div>
      <h1 class="eco-headline">Eco Friendly!</h1>
      <div class="brand-mark-small"><span class="brand-mark-small__dot"></span>Clearhaven</div>
      <p class="usage-note">Replace every 60-90 days.</p>
      <p class="safety-warning">Do not consume! Keep out of reach of children and pets.</p>
    </div>
  </section>
</main>
</body>
</html>
```